Buch-/eBook-Cover zum Thema Magersucht
Zielgruppe
Ich bin Autorin und suche ein passendes Buchcover. Die Zielgruppe für dieses Buch sind Eltern von magersüchtigen Kindern sowie interessierte medizinische und therapeutische Fachkräfte.
Aufgabenstellung
Bei meinem Buch handelt es sich um einen Ratgeber zur Behandlung von Magersucht bei Kindern und Jugendlichen.
Folgendes muss auf die Vorderseite des Buches:
Titel: Brot baut Brücken
Untertitel: Familienbasierte Pflege bei Magersucht
Ilka Momberg
Ich wünsche mir ein einfühlsames Cover, das die Schwere der Krankheit spiegelt, aber auch die Hoffnung auf Heilung. Bitte keine plumpen Bilder von Waage, Massband oder dünnen Körpern.
Der Klappentext im Word-Dokument ist für die Rückseite des Buchcovers.

```html
<!DOCTYPE html>
<html lang="de">
<head>
<meta charset="utf-8">
<title>Brot baut Brücken – Buchcover</title>
<link href="https://fonts.googleapis.com/css2?family=Caveat+Brush&family=Comic+Neue:wght@700&family=Signika:wght@500&display=swap" rel="stylesheet">
<style>
  :root {
    --page-bg: #eeeeee;
    --ink: #354a75;
    --sky-top: #96bed3;
    --sky-mid: #c8e1e6;
    --sky-low: #a8d2e2;
    --sky-bottom: #7db6d0;
    --mint: #bfe6dc;
    --deep-blue: #6fa6c6;
    --wash-dark: #2c4352;
    --wash-teal: #3f6b72;
    --wash-warm: #a89a80;
    --glow: #f1f5e8;
  }
  * { margin: 0; padding: 0; box-sizing: border-box; }
  html, body {
    width: 1200px;
    height: 958px;
    overflow: hidden;
    background: var(--page-bg);
  }
  .canvas {
    position: relative;
    width: 1200px;
    height: 958px;
  }
  .cover {
    position: absolute;
    left: 318px;
    top: 56px;
    width: 563px;
    height: 845px;
    overflow: hidden;
    box-shadow: 4px 5px 8px rgba(0, 0, 0, 0.28);
    background:
      radial-gradient(ellipse 45% 30% at 85% 72%, rgba(191,230,220,0.8) 0%, rgba(191,230,220,0) 100%),
      radial-gradient(ellipse 55% 35% at 5% 95%, rgba(111,166,198,0.85) 0%, rgba(111,166,198,0) 100%),
      radial-gradient(ellipse 60% 40% at 50% 40%, var(--sky-mid) 0%, rgba(200,225,230,0) 100%),
      linear-gradient(180deg, var(--sky-top) 0%, var(--sky-mid) 38%, var(--sky-low) 75%, var(--sky-bottom) 100%);
  }
  .cover-author {
    position: absolute;
    top: 30px;
    width: 100%;
    text-align: center;
    font-family: "Comic Neue", cursive;
    font-weight: 700;
    font-size: 27px;
    letter-spacing: 1px;
    color: var(--ink);
  }
  .cover-title {
    position: absolute;
    top: 116px;
    width: 100%;
    text-align: center;
    font-family: "Caveat Brush", cursive;
    font-weight: 400;
    color: var(--ink);
    line-height: 0.95;
  }
  .title-line {
    display: block;
    white-space: nowrap;
  }
  .title-big { font-size: 100px; }
  .title-small { font-size: 54px; margin-left: 6px; }
  .cover-subtitle {
    position: absolute;
    top: 342px;
    width: 100%;
    text-align: center;
    font-family: "Signika", sans-serif;
    font-weight: 500;
    font-size: 26px;
    color: var(--ink);
  }
  .cover-illustration {
    position: absolute;
    left: 90px;
    top: 410px;
    width: 380px;
    height: 435px;
  }
</style>
</head>
<body>
  <div class="canvas">
    <div class="cover">
      <p class="cover-author">ILKA MOMBERG</p>
      <h1 class="cover-title">
        <span class="title-line"><span class="title-big">BROT</span><span class="title-small">BAUT</span></span>
        <span class="title-line title-big">BRÜCKEN</span>
      </h1>
      <p class="cover-subtitle">Familienbasierte Pflege bei Magersucht</p>
      <svg class="cover-illustration" viewBox="0 0 380 435" role="img" aria-label="Aquarell-Illustration: junge Frau mit langen Haaren in Seitenansicht, mit gesenktem Kopf, vor hellem, blau-grünem Nebel">
        <defs>
          <radialGradient id="halo" cx="50%" cy="35%" r="55%">
            <stop offset="0" stop-color="var(--glow)" stop-opacity="0.95"/>
            <stop offset="0.55" stop-color="var(--glow)" stop-opacity="0.35"/>
            <stop offset="1" stop-color="var(--glow)" stop-opacity="0"/>
          </radialGradient>
          <linearGradient id="wash" x1="0" y1="0" x2="0" y2="1">
            <stop offset="0" stop-color="var(--wash-dark)" stop-opacity="0.85"/>
            <stop offset="0.35" stop-color="var(--wash-teal)" stop-opacity="0.8"/>
            <stop offset="0.55" stop-color="var(--wash-warm)" stop-opacity="0.55"/>
            <stop offset="0.8" stop-color="var(--wash-dark)" stop-opacity="0.8"/>
            <stop offset="1" stop-color="var(--wash-dark)" stop-opacity="0.4"/>
          </linearGradient>
          <filter id="soft" x="-30%" y="-30%" width="160%" height="160%">
            <feGaussianBlur stdDeviation="14"/>
          </filter>
        </defs>
        <ellipse cx="190" cy="170" rx="170" ry="190" fill="url(#halo)"/>
        <rect x="120" y="30" width="140" height="420" rx="70" fill="url(#wash)" filter="url(#soft)"/>
      </svg>
    </div>
  </div>
</body>
</html>
```